Modern Business Card for Larkwell 2018

Our company assumes the best about people. We are creating an online community of entrepreneurs and business leaders who struggle with marketing their business online.

This business card should POP! We recently got a new logo and are launching a new website next month, so our business cards should make a statement that feels:
-Fresh
-Smart
-Trustworthy
-Fun

Target Market(s)

small business owners, entrepreneurs

Industry/Entity Type

Digital Marketing

Contact Information for Business Card

Dimensions: 3.5" x 2"

Font styles to use
Sans Serif

Colors
f37122
ffffff

Requirements
Must have
• We need a business card with a modern, bold design. We will use one side of the card as a lead-generation offer, so text on one side will need to fit up to 140 characters. The business card should stick to our core colors (orange, black, and white).
Nice to have
• We think a vertical "portrait" design could be interesting.
Should not have
• Should not look like a traditional business card. The round icon should stand out from a distance.

```html
<!DOCTYPE html>
<html lang="en">
<head>
<meta charset="utf-8">
<title>Larkwell Business Card</title>
<link rel="stylesheet" href="https://fonts.googleapis.com/css2?family=Montserrat:wght@500;600;700;800&family=Permanent+Marker&display=swap">
<style>
  :root {
    --backdrop: #2348ff;
    --orange: #ff4a0a;
    --orange-light: #ff7a45;
    --white: #ffffff;
    --ink: #111111;
  }
  * { margin: 0; padding: 0; box-sizing: border-box; }
  html, body { width: 1200px; height: 1200px; overflow: hidden; }
  body {
    background: var(--backdrop);
    position: relative;
    font-family: "Montserrat", Arial, sans-serif;
  }
  .card {
    position: absolute;
    left: 234px;
    width: 853px;
    height: 487px;
    background: var(--white);
    border-radius: 50px;
    overflow: hidden;
    transform: scale(0.857);
    transform-origin: 0 0;
  }
  .card--front { top: 137px; }
  .card--back { top: 609px; }
  .card__wave { position: absolute; inset: 0; width: 100%; height: 100%; }

  .brand-mark {
    position: absolute;
    display: flex; flex-direction: column; align-items: center;
  }
  .brand-mark__dot { border-radius: 50%; }
  .brand-mark__name { font-weight: 700; letter-spacing: 1px; }

  .front__mark { left: 417px; top: 34px; width: 200px; }
  .front__mark .brand-mark__dot { width: 120px; height: 120px; background: var(--orange); }
  .front__mark .brand-mark__name { color: var(--orange); font-size: 22px; margin-top: 8px; }

  .front__name {
    position: absolute; left: 240px; right: 40px; top: 228px;
    text-align: center;
    font-family: "Permanent Marker", cursive;
    font-size: 60px; color: var(--orange); letter-spacing: 1px;
  }
  .front__title {
    position: absolute; left: 300px; width: 400px; top: 310px;
    text-align: center; font-weight: 700; font-size: 18px; color: var(--ink);
  }
  .contact {
    position: absolute; display: flex; align-items: center; gap: 8px;
    font-weight: 700; color: var(--ink);
  }
  .contact__icon {
    width: 36px; height: 36px; border-radius: 50%; background: var(--orange);
    display: flex; align-items: center; justify-content: center;
  }
  .front__email { right: 36px; top: 434px; font-size: 30px; }

  .back__wordmark {
    position: absolute; left: 230px; width: 560px; top: 100px;
    text-align: center; font-weight: 800; font-size: 80px; color: var(--orange);
  }
  .back__tagline {
    position: absolute; left: 220px; width: 590px; top: 196px;
    text-align: center; font-family: "Permanent Marker", cursive;
    font-size: 28px; color: var(--ink); letter-spacing: 1px;
  }
  .back__benefits {
    position: absolute; left: 214px; width: 560px; top: 274px;
    display: flex; justify-content: space-between; align-items: baseline;
    list-style: none; font-weight: 700; color: var(--orange);
  }
  .back__benefits li:first-child { font-size: 16px; }
  .back__benefits li { font-size: 13px; }

  .back__mark { left: 14px; top: 322px; width: 160px; }
  .back__mark .brand-mark__dot { width: 100px; height: 100px; background: var(--white); }
  .back__mark .brand-mark__name { color: var(--white); font-size: 24px; margin-top: 18px; }

  .back__offer {
    position: absolute; right: 44px; top: 434px;
    font-size: 9px; color: var(--orange); font-weight: 500;
  }
  .back__url { right: 42px; top: 442px; font-size: 26px; }
</style>
</head>
<body>

<section class="card card--front">
  <svg class="card__wave" viewBox="0 0 853 487" preserveAspectRatio="none" aria-hidden="true">
    <path d="M0 0 H160 C110 60 95 120 120 210 C150 310 250 390 312 487 H0 Z" fill="var(--orange-light)"/>
    <path d="M0 0 H140 C95 70 85 140 130 230 C170 300 210 380 205 487 H0 Z" fill="var(--orange)"/>
    <path d="M0 0 H125 C80 80 110 200 200 310 C240 360 260 420 260 487 H195 C205 380 150 300 115 220 C85 140 90 70 125 0 Z" fill="var(--orange-light)" opacity="0.6"/>
  </svg>
  <div class="brand-mark front__mark">
    <span class="brand-mark__dot"></span>
    <span class="brand-mark__name">LARKWELL</span>
  </div>
  <h1 class="front__name">MARA ELLISON</h1>
  <p class="front__title">STORY MARKETING COACH</p>
  <p class="contact front__email">
    <span class="contact__icon">
      <svg width="20" height="14" viewBox="0 0 20 14" aria-hidden="true"><rect x="1" y="1" width="18" height="12" fill="none" stroke="#fff" stroke-width="2"/><path d="M1 1 L10 8 L19 1" fill="none" stroke="#fff" stroke-width="2"/></svg>
    </span>
    mara@larkwellnow.com
  </p>
</section>

<section class="card card--back">
  <svg class="card__wave" viewBox="0 0 853 487" preserveAspectRatio="none" aria-hidden="true">
    <path d="M0 0 H160 C110 60 95 120 120 210 C150 310 250 390 312 487 H0 Z" fill="var(--orange-light)"/>
    <path d="M0 0 H140 C95 70 85 140 130 230 C170 300 210 380 205 487 H0 Z" fill="var(--orange)"/>
    <path d="M0 0 H125 C80 80 110 200 200 310 C240 360 260 420 260 487 H195 C205 380 150 300 115 220 C85 140 90 70 125 0 Z" fill="var(--orange-light)" opacity="0.6"/>
  </svg>
  <h2 class="back__wordmark">LARKWELL</h2>
  <p class="back__tagline">TELL STORIES THAT INSPIRE ACTION</p>
  <ul class="back__benefits">
    <li>REACH MORE PEOPLE.</li>
    <li>MAKE MORE MONEY.</li>
    <li>CREATE MORE IMPACT.</li>
  </ul>
  <div class="brand-mark back__mark">
    <span class="brand-mark__dot"></span>
    <span class="brand-mark__name">LARKWELL</span>
  </div>
  <p class="back__offer">Get your free Larkwell Starter Package and our marketing guide today at</p>
  <p class="contact back__url">
    <span class="contact__icon">
      <svg width="20" height="20" viewBox="0 0 20 20" aria-hidden="true"><circle cx="10" cy="10" r="8" fill="none" stroke="#fff" stroke-width="1.8"/><ellipse cx="10" cy="10" rx="3.5" ry="8" fill="none" stroke="#fff" stroke-width="1.6"/><path d="M2 10 H18 M3.5 6 H16.5 M3.5 14 H16.5" stroke="#fff" stroke-width="1.4"/></svg>
    </span>
    larkwellnow.com/start
  </p>
</section>

</body>
</html>
```